Modern, sales-driven landing page with video for a photovoltaic configurator

Please create a modern landing page for a photovoltaic configurator where users can select a photovoltaic system, including installation, without entering any personal data. Users can assemble a complete package from our product portfolio and receive a realistic yield and profitability calculation, as well as a complete offer including installation. The landing page should be promoted under the Glanzhof brand (Your Glanzhof Photovoltaic Configurator...). The landing page will be hosted on its own domain: www.glanzhof-energie.de. When submitting an inquiry, users will be redirected to our main website: www.wendel-lichtwerk.de. Text and design suggestions are attached. It is important that both the Glanzhof and Wendel LichtWerk logos are included. Logos are also attached. Various certificates and seals are also included.
Google star ratings and 2-3 customer reviews should be visible. The image should show a tablet with a configurator. Preview images of the configurator and the results (offer, profitability calculation) should be included.

Target Market(s)

homeowners

Coding

Coded - Design and coding required

Font styles to use
Other font styles liked:
• Poppins Bold, Inter

Requirements
Nice to have
• The page should be dark and modern.

```html
<!DOCTYPE html>
<html lang="de">
<head>
<meta charset="utf-8">
<title>Glanzhof – Photovoltaik-Konfigurator</title>
<link href="https://fonts.googleapis.com/css2?family=Poppins:wght@500;600;700&family=Inter:wght@400;500;600&display=swap" rel="stylesheet">
<style>
:root{
  --navy:#0a1524;
  --navy-2:#0f2036;
  --navy-3:#15304f;
  --blue:#2f86e0;
  --blue-light:#4aa2ff;
  --orange:#f29a1f;
  --white:#ffffff;
  --muted:#a8b7c9;
  --dim:#6f8198;
  --board-top:#f4f5fb;
  --board-tint:#dfe4fb;
}
*{box-sizing:border-box;margin:0;padding:0}
html,body{width:1200px;height:5051px;overflow:hidden}
body{position:relative;background:#fff;font-family:"Inter",sans-serif;color:var(--white)}
.board-head{position:absolute;left:0;top:0;width:1200px;height:400px;background:linear-gradient(90deg,var(--board-top) 40%,var(--board-tint))}
.brand{position:absolute;left:0;top:40px;width:1200px;display:flex;flex-direction:column;align-items:center;gap:10px}
.brand-dot{width:92px;height:92px;border-radius:50%;background:var(--blue)}
.brand-name{font-family:"Poppins",sans-serif;font-weight:600;font-size:30px;letter-spacing:2px;color:#1f5fb0}
.mini-brand{display:flex;flex-direction:column;align-items:center;gap:2px}
.mini-brand i{display:block;border-radius:50%;background:var(--blue)}
.mini-brand b{font-family:"Poppins",sans-serif;font-weight:600;color:var(--orange);letter-spacing:.5px}

.desk{position:absolute;left:175px;top:225px;width:593px;background:var(--navy);border-radius:9px 9px 0 0;overflow:hidden;box-shadow:0 0 0 2px #1b2a3f}
.mob{position:absolute;left:804px;top:225px;width:218px;background:var(--navy);border-radius:9px 9px 0 0;overflow:hidden;box-shadow:0 0 0 2px #1b2a3f}
section{position:relative;overflow:hidden}
h1,h2{font-family:"Poppins",sans-serif;font-weight:600;line-height:1.2}
.hl{color:var(--blue-light)}
.or{color:var(--orange)}
.btn{display:inline-block;background:var(--blue);color:#fff;font-weight:600;border-radius:2px;white-space:nowrap}
.btn.orange{background:var(--orange)}
.note{color:var(--dim);font-style:italic}
.photo{background:linear-gradient(160deg,#3d5878,#1c2c43 55%,#5a3f22)}
.ring{border-radius:50%;border:5px solid #23374f;background:radial-gradient(circle at 60% 35%,#f0a040,#8a4a20 35%,#1b2c44 70%)}
.ring.cool{background:radial-gradient(circle at 50% 45%,#6aa6d8,#254766 45%,#101d2e 75%)}
ul.ticks{list-style:none}
ul.ticks li{display:flex;align-items:center;gap:5px}
ul.ticks li::before{content:"";flex:none;border-radius:50%;background:var(--blue)}
.icon{stroke:var(--orange);fill:none;stroke-width:1.6}
strong{color:#fff}

/* ===== DESKTOP ===== */
.d p{font-size:6.5px;color:var(--muted);line-height:1.75}
.d .btn{font-size:5.5px;padding:5px 10px}
.d .note{font-size:5px}
.d h2{font-size:14px}

.d .hero{height:280px;text-align:center}
.d .hero .bg{position:absolute;inset:0;background:linear-gradient(180deg,rgba(10,21,36,.4),rgba(10,21,36,.85)),linear-gradient(120deg,#2a3a4f,#4a4436 50%,#1b2536)}
.d .hero .inner{position:relative;padding-top:14px}
.d .hero h1{font-size:13px;margin-top:68px}
.d .hero .sub{font-size:6px;color:var(--muted);margin-top:6px}
.d .hero .lead{width:250px;margin:18px auto 0;line-height:1.45}
.d .hero .pts{display:flex;justify-content:center;gap:18px;font-size:5px;margin-top:10px}
.d .hero .pts li::before{width:6px;height:6px}
.d .hero .btn{margin-top:10px}
.d .hero .note{margin-top:10px;font-style:normal;color:var(--muted)}
.d .hero .corner{position:absolute;right:10px;bottom:30px}

.d .feature{height:268px;display:flex;align-items:center;justify-content:space-between;padding:0 26px 0 53px}
.d .feature .txt{width:270px}
.d .feature p{margin-top:8px}
.d .feature ul{font-size:5.5px;margin-top:10px;display:flex;flex-direction:column;gap:6px}
.d .feature ul li::before{width:7px;height:7px}
.d .feature .btn{margin-top:10px}
.d .feature .note{margin-top:8px}
.d .feature .ring{width:225px;height:225px;flex:none}
.d .why{height:278px;padding:0 60px 0 55px;background:linear-gradient(180deg,var(--navy),var(--navy-2))}
.d .why .ring{width:200px;height:200px}
.d .why .txt{width:240px}

.d .who{height:330px;text-align:center;background:linear-gradient(180deg,var(--navy-3),#1e3550)}
.d .who h2{margin-top:32px}
.d .who .cols{display:flex;justify-content:center;gap:22px;margin-top:16px}
.d .who .col{width:112px;font-size:5.5px;color:var(--muted);line-height:1.45}
.d .who .col svg{width:13px;height:13px;display:block;margin:0 auto 4px}
.d .who .btn{margin-top:16px}
.d .who .note{margin-top:8px}
.d .who .photo{position:absolute;left:0;bottom:0;width:100%;height:135px;background:linear-gradient(180deg,#1e3550,#2a3442 30%,#3a2e1f 75%,#10151d)}

.d .modules{height:308px;display:flex;align-items:center;gap:45px;padding:0 53px;background:var(--navy)}
.d .modules .txt{width:255px}
.d .modules p{margin-top:10px}
.d .modules .btn{margin-top:12px}
.d .modules .note{margin-top:10px}
.d .frame{position:relative;flex:none}
.d .frame::before{content:"";position:absolute;left:-8px;top:-8px;right:8px;bottom:8px;border:1px solid var(--orange);border-radius:3px}
.d .modules .photo{position:relative;width:188px;height:220px;border-radius:3px;background:linear-gradient(170deg,#8fb7dc,#5d7e55 50%,#2a3c52)}

.d .minutes{height:276px;text-align:center;background:radial-gradient(ellipse at 20% 100%,#7a4b1e 0,transparent 45%),linear-gradient(180deg,#15304f,#0e223a)}
.d .minutes h2{margin-top:34px}
.d .minutes .lbl{font-size:6px;color:var(--orange);margin-top:26px;font-weight:600}
.d .minutes .cards{display:flex;justify-content:center;gap:12px;margin-top:16px}
.d .minutes .card{width:122px;height:64px;background:#17324f;border:1px solid #244566;display:flex;flex-direction:column;align-items:center;justify-content:center;gap:5px;font-size:5px;font-weight:600;line-height:1.3}
.d .minutes .card svg{width:16px;height:16px}
.d .minutes .btn{margin-top:16px}
.d .minutes .note{margin-top:8px}

.d .funding{height:308px;display:flex;align-items:center;gap:45px;padding:0 60px;background:linear-gradient(180deg,#0c1828,var(--navy))}
.d .funding .photo{position:relative;width:190px;height:222px;border-radius:3px;background:linear-gradient(170deg,#3c4a60,#5a4a34 55%,#1a1f28)}
.d .funding .txt{width:245px}
.d .funding p{margin-top:8px}
.d .funding .tip{font-size:6px;color:var(--orange);margin-top:8px;font-weight:600}
.d .funding p.small{font-size:5.2px;margin-top:4px}
.d .funding .btn{margin-top:10px}

.d .next{height:278px;text-align:center;background:var(--navy-2)}
.d .next h2{margin-top:36px}
.d .next .sub{font-size:6px;color:var(--muted);margin-top:8px}
.d .next .circles{display:flex;justify-content:center;gap:28px;margin-top:18px}
.d .next .circle{width:74px;height:74px;border-radius:50%;background:#15304f;border:1px solid #22415f;display:flex;flex-direction:column;align-items:center;justify-content:center;gap:6px;font-size:5px;font-weight:600}
.d .next .circle svg{width:15px;height:15px}
.d .next .btn{margin-top:18px}
.d .next .note{margin-top:8px}

.d .cta{height:216px;padding:34px 53px;background:linear-gradient(100deg,#2e6aa8,#1a3a5e 60%,#0f2038)}
.d .cta h2{font-size:18px;width:350px;line-height:1.15}
.d .cta .btn{margin-top:16px}
.d .cta .note{margin-top:8px;color:var(--muted)}
.d footer{height:31px;display:flex;align-items:center;justify-content:space-between;padding:0 53px;background:#0d1a2a;font-size:5px;color:var(--muted)}
.social{display:flex;gap:4px}
.social i{display:block;border-radius:50%;border:1px solid var(--dim)}
.d .social i{width:10px;height:10px}

/* ===== MOBILE ===== */
.m section{padding:0 10px}
.m h2{font-size:17px}
.m p{font-size:7.5px;color:var(--muted);line-height:2}
.m ul.ticks li{font-size:6.3px;color:#fff;font-weight:600;line-height:1.5}
.m ul.ticks li::before{width:7px;height:7px}
.m .btn{font-size:6.3px;padding:6px 9px}
.m .note{font-size:6px;line-height:1.8}
.m .center{text-align:center}

.m .hero{height:343px;text-align:center;padding-top:12px}
.m .hero .bg{position:absolute;inset:0;background:linear-gradient(180deg,rgba(10,21,36,.35),rgba(10,21,36,.9)),linear-gradient(140deg,#34445a,#4a4234 55%,#1a2436)}
.m .hero .inner{position:relative}
.m .hero h1{font-size:17px;margin-top:16px}
.m .hero .sub{font-size:6.3px;color:var(--muted);margin-top:8px;line-height:1.6}
.m .hero .lead{margin-top:10px;line-height:1.5}
.m .hero ul{margin-top:8px;display:flex;flex-direction:column;gap:6px}
.m .hero ul li{font-size:5.8px}
.m .hero .btn{margin-top:14px}
.m .hero .note{font-style:normal;color:var(--muted);margin-top:10px;font-size:5.5px}

.m .what{height:333px;padding-top:24px}
.m .what p{margin-top:8px}
.m .what ul{margin-top:10px;display:flex;flex-direction:column;gap:8px}
.m .what .note{margin-top:10px}
.m .what .btn{margin-top:10px}

.m .why{height:755px;background:linear-gradient(180deg,var(--navy),var(--navy-2))}
.m .ring{width:190px;height:190px;margin:0 auto}
.m .why .ring{margin-top:6px}
.m .why h2{margin-top:22px}
.m .why p{margin-top:10px}
.m .why ul{margin-top:10px;display:flex;flex-direction:column;gap:10px}
.m .why .btn{margin-top:14px}
.m .why .note{margin-top:8px}
.m .why .ring.cool{margin-top:34px}

.m .who{height:470px;text-align:center;background:linear-gradient(180deg,#15304f,#1e3550)}
.m .who .txt{position:relative}
.m .who h2{margin-top:20px}
.m .who .item{margin-top:16px}
.m .who .item svg{width:16px;height:16px;display:block;margin:0 auto 4px}
.m .who .item p{line-height:1.7}
.m .who .btn{margin-top:14px}
.m .who .note{margin-top:6px}
.m .who .photo{position:absolute;left:0;bottom:0;width:100%;height:150px;background:linear-gradient(180deg,#1e3550,#2a3442 30%,#3a2e1f 80%,#10151d)}

.m .modules{height:608px;background:var(--navy)}
.m .modules h2{margin-top:16px}
.m .modules p{margin-top:8px;font-size:8px}
.m .modules .btn{margin-top:10px}
.m .modules .note{margin-top:10px}
.m .modules .photo{width:172px;height:222px;margin:16px auto 0;border-radius:3px;background:linear-gradient(170deg,#8fb7dc,#5d7e55 50%,#2a3c52)}

.m .minutes{height:530px;text-align:center;background:linear-gradient(180deg,#15304f,#0e223a)}
.m .minutes h2{margin-top:22px}
.m .minutes .lbl{font-size:6.5px;color:var(--orange);font-weight:600;margin-top:6px}
.m .minutes .card{width:198px;height:104px;margin-top:14px;background:#17324f;border:1px solid #244566;display:flex;flex-direction:column;align-items:center;justify-content:center;gap:10px;font-size:6.5px;font-weight:600;line-height:1.4}
.m .minutes .card svg{width:26px;height:26px}
.m .minutes .btn{margin-top:16px;background:#3a7bd0}
.m .minutes .note{margin-top:6px}

.m .funding{height:540px;text-align:center;background:linear-gradient(180deg,#3a2714,#0c1828 45%,var(--navy))}
.m .funding h2{margin-top:18px}
.m .funding p{margin-top:6px}
.m .funding .tip{font-size:7px;color:var(--orange);font-weight:600;margin-top:4px}
.m .funding p.small{font-size:6.5px}
.m .funding .btn{margin-top:10px}
.m .funding .photo{width:172px;height:190px;margin:30px auto 0;border-radius:3px;border:1px solid #2a4262;background:linear-gradient(170deg,#3c4a60,#5a4a34 55%,#1a1f28)}

.m .next{height:775px;text-align:center;background:var(--navy-2)}
.m .next h2{margin-top:22px}
.m .next p{margin-top:8px;line-height:1.8}
.m .next .circle{width:165px;height:165px;border-radius:50%;margin:26px auto 0;background:#15304f;border:1px solid #22415f;display:flex;flex-direction:column;align-items:center;justify-content:center;gap:12px;font-size:6.5px;font-weight:600}
.m .next .circle svg{width:28px;height:28px}
.m .next .btn{margin-top:30px}
.m .next .note{margin-top:10px}

.m .cta{height:230px;text-align:center;padding-top:22px;background:linear-gradient(180deg,#2e6aa8,#1a3a5e)}
.m .cta h2{font-size:17px;line-height:1.2}
.m .cta .btn{margin-top:12px}
.m .cta .note{margin-top:4px;color:var(--muted)}
.m footer{height:88px;text-align:center;padding-top:22px;background:#0d1a2a;font-size:5.5px;color:var(--muted)}
.m .social{justify-content:center;gap:6px}
.m .social i{width:14px;height:14px}
.m footer .copy{margin-top:16px}
.m .sticky{height:31px;background:var(--orange);display:flex;align-items:center;justify-content:center;font-size:7px;font-weight:600}
</style>
</head>
<body>
<div class="board-head"></div>
<div class="brand"><span class="brand-dot"></span><span class="brand-name">GLANZHOF</span></div>

<main class="desk d">
  <section class="hero">
    <div class="bg" role="img" aria-label="Foto: modernes Einfamilienhaus mit Solardach in der Abenddämmerung"></div>
    <div class="inner">
      <div class="mini-brand"><i style="width:14px;height:14px"></i><b style="font-size:5px">GLANZHOF</b></div>
      <h1>Ihre Photovoltaikanlage - ehrlich kalkuliert.</h1>
      <div class="sub">Mit dem GLANZHOF Photovoltaik-Konfigurator.</div>
      <p class="lead">Konfigurieren Sie Ihre Solaranlage in wenigen Schritten – für Einfamilienhaus, Gewerbehalle oder alles dazwischen.</p>
      <ul class="ticks pts">
        <li>Ergebnis ohne Angabe persönlicher Daten</li>
        <li>Für private &amp; gewerbliche Dächer jeder Größe</li>
        <li>Realistische Einschätzung statt Lockpreise</li>
      </ul>
      <span class="btn">Jetzt PV-Anlage konfigurieren</span>
      <div class="note">Ohne Registrierung · Ohne Kontaktdaten · Kostenlos</div>
    </div>
    <span class="btn orange corner">Konfigurator starten</span>
  </section>

  <section class="feature">
    <div class="txt">
      <h2>Was kann der <span class="hl">Solar-Konfigurator?</span></h2>
      <p>Sie legen die Eckdaten fest – wir liefern eine <strong>nachvollziehbare Auswertung</strong> zu:</p>
      <ul class="ticks">
        <li>möglicher Anlagengröße</li>
        <li>passenden Modulen, Wechselrichtern &amp; Energiespeichern</li>
        <li>realistischer Wirtschaftlichkeit</li>
      </ul>
      <div class="note">Ohne Registrierung. Ohne Telefonterror. Ohne versteckte Agenda.</div>
      <span class="btn">Jetzt persönliche PV-Auswertung erhalten</span>
      <div class="note">Ergebnis sofort sichtbar – ohne Datenangabe</div>
    </div>
    <div class="ring" role="img" aria-label="Illustration: Sonne und Solarmodul in runder Fensteransicht"></div>
  </section>

  <section class="feature why">
    <div class="ring cool" role="img" aria-label="Illustration: Tablet mit Konfigurator in runder Fensteransicht"></div>
    <div class="txt">
      <h2>Warum unser<br><span class="hl">Konfigurator anders ist</span></h2>
      <p>Viele Solarrechner zeigen Ergebnisse erst nach Eingabe Ihrer Kontaktdaten. Wir zeigen Ihr</p>
      <p class="or" style="font-weight:600;margin-top:2px">Ergebnis zuerst.</p>
      <ul class="ticks">
        <li>Keine Datensammlung</li>
        <li>Kein Verkaufsdruck</li>
        <li>Keine künstlich niedrigen Einstiegspreise</li>
      </ul>
      <span class="btn">Ergebnis ohne Daten sehen</span>
      <div class="note">Keine E-Mail. Kein Telefon. Keine Verpflichtung.</div>
    </div>
  </section>

  <section class="who">
    <div class="photo" role="img" aria-label="Foto: Haus mit großer Solaranlage auf dem Dach bei Dämmerung"></div>
    <div style="position:relative">
      <h2>Für wen eignet <span class="hl">sich der Konfigurator?</span></h2>
      <div class="cols">
        <div class="col"><svg class="icon" viewBox="0 0 12 12"><path d="M1 6 6 2l5 4M2.5 5v6h7V5"/></svg>Privathaushalte – Neubau oder Bestandsgebäude</div>
        <div class="col"><svg class="icon" viewBox="0 0 12 12"><rect x="2" y="1.5" width="8" height="9.5"/><path d="M4 4h4M4 6h4M4 8h4"/></svg>vom Handwerksbetrieb bis zur industriellen Gewerbebetriebe</div>
        <div class="col"><svg class="icon" viewBox="0 0 12 12"><rect x="1.5" y="2" width="9" height="8"/><path d="M1.5 5h9M1.5 7.5h9M4.5 2v8M7.5 2v8"/></svg>Kleine Dachflächen ebenso wie große Hallendächer</div>
        <div class="col"><svg class="icon" viewBox="0 0 12 12"><path d="M6 1 11 6 6 11 1 6z"/><circle cx="6" cy="6" r="1.5"/></svg>Für alle, die <strong>echte Zahlen</strong> statt Verkaufsversprechen wollen</div>
      </div>
      <span class="btn">Ergebnis ohne Daten sehen</span>
      <div class="note">Direkt, unverbindlich, anonym</div>
    </div>
  </section>

  <section class="modules">
    <div class="txt">
      <h2>Module &amp; Komponenten -<br><span class="hl">Sie haben die Wahl</span></h2>
      <p>Im Konfigurator wählen Sie: Solarmodule, Wechselrichter, optional Energiespeicher. Preisunterschiede sind gering – Entscheidung nach Design, Effizienz und persönlichen Prioritäten.</p>
      <p><strong>Keine Kaufempfehlung mit Verkaufsdruck nur transparente Optionen.</strong></p>
      <span class="btn">Module &amp; Speicher selbst auswählen</span>
      <div class="note">Preis &amp; Wirtschaftlichkeit passen sich automatisch an</div>
    </div>
    <div class="frame"><div class="photo" role="img" aria-label="Foto: Familie neben Solarmodulen im Garten vor ihrem Haus"></div></div>
  </section>

  <section class="minutes">
    <h2>In wenigen Minuten <span class="hl">zu Ihrem Preis</span></h2>
    <div class="lbl">Erhalten Sie sofort:</div>
    <div class="cards">
      <div class="card"><svg class="icon" viewBox="0 0 16 16"><rect x="3" y="2" width="10" height="12"/><path d="M5 5h6M5 8h6M5 11h4"/></svg>Realistischen Angebotspreis</div>
      <div class="card"><svg class="icon" viewBox="0 0 16 16"><path d="M2 14h12M4 13V9M7 13V6M10 13V8M13 13V4"/></svg>Ertrags- und<br>Wirtschaftlichkeitsanalyse</div>
      <div class="card"><svg class="icon" viewBox="0 0 16 16"><path d="M3 13 13 3M3 3l10 10"/><circle cx="8" cy="8" r="2"/></svg>Modernes, schlüsselfertiges<br>Solarkonzept</div>
    </div>
    <span class="btn">PV-Ergebnis jetzt sehen</span>
    <div class="note">Einfach, anonym, kostenlos</div>
  </section>

  <section class="funding">
    <div class="frame"><div class="photo" role="img" aria-label="Foto: modernes Haus mit Solardach in der Abendsonne"></div></div>
    <div class="txt">
      <h2>Hinweis zu <span class="hl">Förderungen</span></h2>
      <p>Kommunale Förderprogramme können die Wirtschaftlichkeit verbessern. Da sie regional unterschiedlich sind, können wir keine Gewähr übernehmen.</p>
      <div class="tip">Tipp:</div>
      <p class="small">Prüfen Sie Förderangebote direkt auf der Website Ihrer Kommune oder telefonisch. Hinweis: Förderkonditionen können jederzeit angepasst oder eingestellt werden.</p>
      <span class="btn">Konfigurator starten</span>
    </div>
  </section>

  <section class="next">
    <h2>Nächster Schritt? <span class="hl">Nur wenn Sie möchten.</span></h2>
    <div class="sub">Hat Ihr Ergebnis Fragen aufgeworfen oder möchten Sie wissen, wie sich die Anlage konkret umsetzen lässt?</div>
    <div class="circles">
      <div class="circle"><svg class="icon" viewBox="0 0 14 14"><circle cx="7" cy="4" r="2"/><path d="M3 12c0-3 8-3 8 0"/></svg>Persönliche Beratung</div>
      <div class="circle"><svg class="icon" viewBox="0 0 14 14"><path d="M3 8V6a4 4 0 0 1 8 0v2"/><rect x="2" y="8" width="2" height="3"/><rect x="10" y="8" width="2" height="3"/></svg>Klare Antworten</div>
      <div class="circle"><svg class="icon" viewBox="0 0 14 14"><rect x="2" y="3" width="10" height="8"/><path d="M5 7h4"/></svg>Keine Verkaufsshows</div>
    </div>
    <span class="btn">Beratung anfragen</span>
    <div class="note">Freiwillig. Persönlich. Keine Verkaufsshows.</div>
  </section>

  <section class="cta" role="img" aria-label="Hintergrund: Haus mit Solardach in blauer Abendstimmung">
    <h2><span class="or">Photovoltaik ist eine Investition für Jahrzehnte.</span> Deshalb sollte sie verstanden werden - nicht verkauft.</h2>
    <span class="btn orange">PV-Konfigurator jetzt starten</span>
    <div class="note">Kostenlos. Anonym. Unverbindlich.</div>
  </section>

  <footer>
    <span>Copyright © 2026 <span class="hl">Glanzhof</span>. All rights reserved.</span>
    <span class="social"><i></i><i></i><i></i><i></i><i></i></span>
  </footer>
</main>

<main class="mob m">
  <section class="hero">
    <div class="bg" role="img" aria-label="Foto: Einfamilienhaus mit Solardach in der Dämmerung"></div>
    <div class="inner">
      <div class="mini-brand"><i style="width:16px;height:16px"></i><b style="font-size:5.5px">GLANZHOF</b></div>
      <h1>Ihre<br>Photovoltaikanlage -<br>ehrlich kalkuliert.</h1>
      <div class="sub">Mit dem GLANZHOF Photovoltaik-Konfigurator.</div>
      <p class="lead">Konfigurieren Sie Ihre Solaranlage in wenigen Schritten – für Einfamilienhaus, Gewerbehalle oder alles dazwischen.</p>
      <ul class="ticks">
        <li>Für private &amp; gewerbliche Dächer jeder Größe</li>
        <li>Ergebnis ohne Angabe persönlicher Daten</li>
        <li>Realistische Einschätzung statt Lockpreise</li>
      </ul>
      <span class="btn">Jetzt PV-Anlage konfigurieren</span>
      <div class="note">Ohne Registrierung · Ohne Kontaktdaten · Kostenlos</div>
    </div>
  </section>

  <section class="what">
    <h2>Was kann der <span class="hl">Solar-Konfigurator?</span></h2>
    <p>Sie legen die Eckdaten fest – wir liefern eine <strong>nachvollziehbare Auswertung</strong> zu:</p>
    <ul class="ticks">
      <li>möglicher Anlagengröße</li>
      <li>passenden Modulen, Wechselrichtern &amp; Energiespeichern</li>
      <li>realistischer Wirtschaftlichkeit</li>
    </ul>
    <div class="note">Ohne Registrierung. Ohne Telefonterror. Ohne versteckte Agenda.</div>
    <span class="btn">Jetzt persönliche PV-Auswertung erhalten</span>
    <div class="note">Ergebnis sofort sichtbar – ohne Datenangabe</div>
  </section>

  <section class="why">
    <div class="ring" role="img" aria-label="Illustration: Sonne und Solarmodul in runder Fensteransicht"></div>
    <h2>Warum unser <span class="hl">Konfigurator anders ist</span></h2>
    <p>Viele Solarrechner zeigen Ergebnisse erst nach Eingabe Ihrer Kontaktdaten. Wir zeigen Ihr</p>
    <p class="or" style="font-weight:600;margin-top:4px">Ergebnis zuerst.</p>
    <ul class="ticks">
      <li>Keine Datensammlung</li>
      <li>Kein Verkaufsdruck</li>
      <li>Keine künstlich niedrigen Einstiegspreise</li>
    </ul>
    <span class="btn">Ergebnis ohne Daten sehen</span>
    <div class="note">Keine E-Mail. Kein Telefon. Keine Verpflichtung.</div>
    <div class="ring cool" role="img" aria-label="Illustration: Tablet mit Konfigurator in runder Fensteransicht"></div>
  </section>

  <section class="who">
    <div class="photo" role="img" aria-label="Foto: Haus mit Solaranlage auf dem Dach bei Dämmerung"></div>
    <div class="txt">
      <h2>Für wen eignet <span class="hl">sich der Konfigurator?</span></h2>
      <div class="item"><svg class="icon" viewBox="0 0 12 12"><path d="M1 6 6 2l5 4M2.5 5v6h7V5"/></svg><p>Privathaushalte – Neubau oder<br>Bestandsgebäude</p></div>
      <div class="item"><svg class="icon" viewBox="0 0 12 12"><rect x="2" y="1.5" width="8" height="9.5"/><path d="M4 4h4M4 6h4M4 8h4"/></svg><p>vom Handwerksbetrieb bis<br>zur industriellen Gewerbebetriebe</p></div>
      <div class="item"><svg class="icon" viewBox="0 0 12 12"><rect x="1.5" y="2" width="9" height="8"/><path d="M1.5 5h9M1.5 7.5h9M4.5 2v8M7.5 2v8"/></svg><p>Kleine Dachflächen ebenso wie große Hallendächer</p></div>
      <div class="item"><svg class="icon" viewBox="0 0 12 12"><path d="M6 1 11 6 6 11 1 6z"/><circle cx="6" cy="6" r="1.5"/></svg><p>Für alle, die <strong>echte Zahlen</strong><br>statt Verkaufsversprechen wollen</p></div>
      <span class="btn">Ergebnis ohne Daten sehen</span>
      <div class="note">Direkt, unverbindlich, anonym</div>
    </div>
  </section>

  <section class="modules center">
    <h2>Module &amp; Komponenten - <span class="hl">Sie haben die Wahl</span></h2>
    <p>Im Konfigurator wählen Sie: Solarmodule, Wechselrichter, optional Energiespeicher. Preisunterschiede sind gering – Entscheidung nach Design, Effizienz und persönlichen Prioritäten.</p>
    <p><strong>Keine Kaufempfehlung mit Verkaufsdruck nur transparente Optionen.</strong></p>
    <span class="btn">Module &amp; Speicher selbst auswählen</span>
    <div class="note">Preis &amp; Wirtschaftlichkeit passen sich automatisch an</div>
    <div class="photo" role="img" aria-label="Foto: Familie neben Solarmodulen im Garten vor ihrem Haus"></div>
  </section>

  <section class="minutes">
    <h2>In wenigen Minuten <span class="hl">zu Ihrem Preis</span></h2>
    <div class="lbl">Erhalten Sie sofort:</div>
    <div class="card"><svg class="icon" viewBox="0 0 16 16"><rect x="3" y="2" width="10" height="12"/><path d="M5 5h6M5 8h6M5 11h4"/></svg>Realistischen Angebotspreis</div>
    <div class="card"><svg class="icon" viewBox="0 0 16 16"><path d="M2 14h12M4 13V9M7 13V6M10 13V8M13 13V4"/></svg>Ertrags- und<br>Wirtschaftlichkeitsanalyse</div>
    <div class="card"><svg class="icon" viewBox="0 0 16 16"><path d="M3 13 13 3M3 3l10 10"/><circle cx="8" cy="8" r="2"/></svg>Modernes, schlüsselfertiges<br>Solarkonzept</div>
    <span class="btn">PV-Ergebnis jetzt sehen</span>
    <div class="note">Einfach, anonym, kostenlos</div>
  </section>

  <section class="funding">
    <h2>Hinweis zu <span class="hl">Förderungen</span></h2>
    <p>Kommunale Förderprogramme können die Wirtschaftlichkeit verbessern. Da sie regional unterschiedlich sind, können wir keine Gewähr übernehmen.</p>
    <div class="tip">Tipp:</div>
    <p class="small">Prüfen Sie Förderangebote direkt auf der Website Ihrer Kommune oder telefonisch. Hinweis: Förderkonditionen können jederzeit angepasst oder eingestellt werden.</p>
    <span class="btn">Konfigurator starten</span>
    <div class="photo" role="img" aria-label="Foto: modernes Haus mit Solardach in der Abendsonne"></div>
  </section>

  <section class="next">
    <h2>Nächster Schritt? <span class="hl">Nur wenn Sie möchten.</span></h2>
    <p>Hat Ihr Ergebnis Fragen aufgeworfen oder möchten Sie wissen, wie sich die Anlage konkret umsetzen lässt?</p>
    <div class="circle"><svg class="icon" viewBox="0 0 14 14"><circle cx="7" cy="4" r="2"/><path d="M3 12c0-3 8-3 8 0"/></svg>Persönliche Beratung</div>
    <div class="circle"><svg class="icon" viewBox="0 0 14 14"><path d="M3 8V6a4 4 0 0 1 8 0v2"/><rect x="2" y="8" width="2" height="3"/><rect x="10" y="8" width="2" height="3"/></svg>Klare Antworten</div>
    <div class="circle"><svg class="icon" viewBox="0 0 14 14"><rect x="2" y="3" width="10" height="8"/><path d="M5 7h4"/></svg>Keine Verkaufsshows</div>
    <span class="btn">Beratung anfragen</span>
    <div class="note">Freiwillig. Persönlich. Keine Verkaufsshows.</div>
  </section>

  <section class="cta" role="img" aria-label="Hintergrund: Haus mit Solardach in blauer Abendstimmung">
    <h2><span class="or">Photovoltaik ist eine Investition für Jahrzehnte.</span> Deshalb sollte sie verstanden werden - nicht verkauft.</h2>
    <span class="btn orange">PV-Konfigurator jetzt starten</span>
    <div class="note">Kostenlos. Anonym. Unverbindlich.</div>
  </section>

  <footer>
    <div class="social"><i></i><i></i><i></i><i></i><i></i></div>
    <div class="copy">Copyright © 2026 <span class="hl">Glanzhof</span>. All rights reserved.</div>
  </footer>
  <div class="sticky">Konfigurator starten</div>
</main>
</body>
</html>
```